Tavenorix - world unique technology for better life - please let them know who am i at first sight

We need a new business card for company which is a provider of unique crystal based technology suitable for all living being. For more information and final design you can use our brochure (our colours are black and blue from brochure).
We use Verdana font

Industry/Entity Type

Business

Contact Information for Business Card

regular dimension

Font styles to use
Other font styles liked:
• Verdana

Requirements
Must have
• Logo
• name
• function/position
• phone
• mobile
• e-mail
• adress
Nice to have
• inovative design (technology directed)

```html
<!DOCTYPE html>
<html lang="en">
<head>
<meta charset="utf-8">
<title>Tavenorix – Business Card</title>
<link rel="stylesheet" href="https://fonts.googleapis.com/css2?family=Open+Sans:wght@300;400;700&display=swap">
<style>
  :root {
    --page-bg: #e6e8ea;
    --card-black: #050708;
    --pattern-tone: #14202a;
    --brand-blue: #1aa1e0;
    --card-blue: #2eaee6;
    --text-white: #ffffff;
    --divider: #3a444c;
  }
  * { box-sizing: border-box; margin: 0; padding: 0; }
  html, body {
    width: 1200px; height: 1000px; overflow: hidden;
    background: var(--page-bg);
    font-family: "Open Sans", Verdana, sans-serif;
  }
  .sheet {
    width: 1200px; height: 1000px;
    display: flex; flex-direction: column;
    align-items: center; justify-content: center; gap: 60px;
  }
  .card {
    position: relative;
    width: 700px; height: 400px;
    border-radius: 4px;
    overflow: hidden;
    box-shadow: 0 6px 18px rgba(0,0,0,0.18);
  }
  /* Front: contact side */
  .card--front { background: var(--card-black); color: var(--text-white); }
  .card__pattern {
    position: absolute; inset: 0;
    background: radial-gradient(circle at 68% 55%, var(--pattern-tone) 0%, #0b1218 45%, var(--card-black) 85%);
  }
  .card__divider {
    position: absolute; left: 350px; top: 60px; bottom: 60px;
    width: 1px; background: var(--divider);
  }
  .contact {
    position: absolute; left: 56px; top: 70px;
  }
  .contact__name {
    color: var(--brand-blue); font-weight: 700; font-size: 26px; line-height: 1.1;
  }
  .contact__role {
    font-weight: 700; font-size: 22px; margin-bottom: 22px;
  }
  .contact__list { list-style: none; }
  .contact__item {
    display: flex; align-items: flex-start; gap: 14px;
    font-size: 18px; line-height: 1.45; margin-bottom: 4px;
  }
  .contact__icon { width: 20px; height: 20px; flex: none; margin-top: 3px; }
  .logo {
    display: flex; align-items: center; gap: 14px;
  }
  .logo__dot { border-radius: 50%; flex: none; }
  .logo__name { font-weight: 300; letter-spacing: 0.04em; }
  .card--front .logo {
    position: absolute; left: 410px; top: 170px;
  }
  .card--front .logo__dot { width: 46px; height: 46px; background: var(--text-white); }
  .card--front .logo__name { font-size: 34px; color: var(--text-white); }
  /* Back: brand side */
  .card--back {
    background: var(--card-blue);
    display: flex; align-items: center; justify-content: center;
  }
  .card--back .logo__dot { width: 90px; height: 90px; background: var(--text-white); }
  .card--back .logo__name { font-size: 60px; color: var(--text-white); }
</style>
</head>
<body>
<main class="sheet">
  <section class="card card--front" aria-label="Business card front">
    <div class="card__pattern" role="img" aria-label="Dark blue crystal lattice pattern across the card"></div>
    <div class="card__divider"></div>
    <div class="contact">
      <p class="contact__name">Marek Lind</p>
      <p class="contact__role">CEO</p>
      <ul class="contact__list">
        <li class="contact__item">
          <svg class="contact__icon" viewBox="0 0 20 20" aria-label="Phone"><path d="M4 3h4l1.5 4-2 1.5a10 10 0 0 0 4 4l1.5-2 4 1.5v4a2 2 0 0 1-2 2A15 15 0 0 1 2 5a2 2 0 0 1 2-2z" fill="none" stroke="var(--brand-blue)" stroke-width="1.8"/></svg>
          <span>(0) 246813579</span>
        </li>
        <li class="contact__item">
          <svg class="contact__icon" viewBox="0 0 20 20" aria-label="Mobile"><rect x="5" y="1.5" width="10" height="17" rx="1.5" fill="none" stroke="var(--brand-blue)" stroke-width="1.8"/><line x1="8.5" y1="15.5" x2="11.5" y2="15.5" stroke="var(--brand-blue)" stroke-width="1.5"/></svg>
          <span>(0) 246813579</span>
        </li>
        <li class="contact__item">
          <svg class="contact__icon" viewBox="0 0 20 20" aria-label="Email"><rect x="1.5" y="4" width="17" height="12" fill="var(--brand-blue)"/><path d="M1.5 4l8.5 7 8.5-7" fill="none" stroke="var(--card-black)" stroke-width="1.4"/></svg>
          <span>hello@tavenorix.com</span>
        </li>
        <li class="contact__item">
          <svg class="contact__icon" viewBox="0 0 20 20" aria-label="Address"><path d="M10 1.5a6 6 0 0 1 6 6c0 4.5-6 11-6 11s-6-6.5-6-11a6 6 0 0 1 6-6z" fill="var(--brand-blue)"/><circle cx="10" cy="7.5" r="2.2" fill="var(--card-black)"/></svg>
          <span>27 Harbour Rd<br>Town, City</span>
        </li>
      </ul>
    </div>
    <div class="logo">
      <span class="logo__dot"></span>
      <span class="logo__name">TAVENORIX</span>
    </div>
  </section>

  <section class="card card--back" aria-label="Business card back">
    <div class="logo">
      <span class="logo__dot"></span>
      <span class="logo__name">TAVENORIX</span>
    </div>
  </section>
</main>
</body>
</html>
```